sydney wedding photography business needs a business card design

we need a business card design for a sydney based wedding photography and videography business. our business name is :golden hour photography and video. our target clients are 24-35 yrs female. our style is candid, organic, natural, dynamic. we are a team of young photographers and videographers, and help brides to create memories that they will cherish for the rest of their lives. the logo will be provided. we want an elegant design that reflects our style, and also want to give a great impression to our clients that we are one of the best studios in sydney and our brand means quality and premium service.

Target Market(s)

bride to be, 24-35 years old, living in sydney and surrunding areas

Industry/Entity Type

Wedding Photography

Contact Information for Business Card

address: 57 marrow lane, bexton nsw 2041
mobile: 0431872056
phone: (02) 9361 2748
info@goldenhourstudio.net.au
www.goldenhourstudio.net.au
facebook:goldenhourbridals
instagram:goldenhourbridals

Font styles to use
Serif
Sans Serif

Requirements
Nice to have
• maybe add my slogan"memories beyond eternity" if the layout looks good
Should not have
• no black color, not good idea for wedding biz card

```html
<!DOCTYPE html>
<html lang="en">
<head>
<meta charset="utf-8">
<title>Golden Hour Photography and Video – Business Card</title>
<link rel="stylesheet" href="https://fonts.googleapis.com/css2?family=Source+Sans+3:wght@400;600&display=swap">
<style>
  :root {
    --page-bg: #e8e5e0;
    --card-top: #f4f1ee;
    --card-top-edge: #ebe6e2;
    --band: #5a4d44;
    --gold: #dba41c;
    --text-light: #f6f1ea;
  }
  * { box-sizing: border-box; margin: 0; padding: 0; }
  html, body {
    width: 1200px; height: 900px; overflow: hidden;
    background: var(--page-bg);
    font-family: "Source Sans 3", "Myriad Pro", Arial, sans-serif;
  }
  .card {
    position: absolute; left: 110px; top: 147px;
    width: 980px; height: 605px;
    box-shadow: 0 18px 40px rgba(0,0,0,.18);
    overflow: hidden;
  }
  .card-top {
    position: absolute; left: 0; top: 0; width: 100%; height: 328px;
    background: linear-gradient(180deg, var(--card-top) 0%, var(--card-top-edge) 100%);
  }
  .brand {
    position: absolute; left: 0; right: 0; top: 120px;
    text-align: center; color: var(--gold); font-weight: 600;
  }
  .brand-name { font-size: 84px; line-height: 1; letter-spacing: 1px; }
  .brand-sub { margin-top: 22px; font-size: 30px; letter-spacing: 14px; }
  .card-band {
    position: absolute; left: 0; top: 328px; width: 100%; height: 277px;
    background: var(--band);
  }
  .person { position: absolute; left: 60px; top: 52px; color: var(--text-light); }
  .person-name { color: var(--gold); font-size: 31px; font-weight: 600; line-height: 1.1; }
  .person-title { font-size: 25px; line-height: 1.3; }
  .address { margin-top: 38px; font-size: 25px; line-height: 1.38; }
  .contacts {
    position: absolute; right: 40px; top: 38px;
    color: var(--text-light); font-size: 25px; text-align: right;
  }
  .contact-line { display: flex; justify-content: flex-end; align-items: center; gap: 14px; height: 34px; }
  .contact-line svg { width: 20px; height: 20px; fill: var(--gold); flex: none; }
  .social { margin-top: 16px; }
  .social-dot { width: 20px; height: 20px; border-radius: 50%; background: var(--gold); flex: none; }
</style>
</head>
<body>
  <div class="card">
    <div class="card-top">
      <div class="brand">
        <div class="brand-name">Golden Hour</div>
        <div class="brand-sub">PHOTOGRAPHY AND VIDEO</div>
      </div>
    </div>
    <div class="card-band">
      <div class="person">
        <div class="person-name">Daniel Hartley</div>
        <div class="person-title">Managing Director</div>
        <div class="address">57 Marrow Lane,<br>Bexton NSW 2041.</div>
      </div>
      <div class="contacts">
        <div class="contact-line">0431 872 056
          <svg viewBox="0 0 24 24" aria-hidden="true"><rect x="6" y="2" width="12" height="20" rx="2.5"/><rect x="8" y="5" width="8" height="12" fill="var(--band)"/><circle cx="12" cy="19.3" r="1.1" fill="var(--band)"/></svg>
        </div>
        <div class="contact-line">(02) 9361 2748
          <svg viewBox="0 0 24 24" aria-hidden="true"><path d="M6.6 10.8a15.1 15.1 0 0 0 6.6 6.6l2.2-2.2a1 1 0 0 1 1-.25 11.4 11.4 0 0 0 3.6.57 1 1 0 0 1 1 1V20a1 1 0 0 1-1 1A17 17 0 0 1 3 4a1 1 0 0 1 1-1h3.5a1 1 0 0 1 1 1c0 1.25.2 2.450.57 3.57a1 1 0 0 1-.25 1z"/></svg>
        </div>
        <div class="contact-line">info@goldenhourstudio.net.au
          <svg viewBox="0 0 24 24" aria-hidden="true"><path d="M3 6h18v12H3z"/><path d="M3.5 6.5l8.5 6.6 8.5-6.6" fill="none" stroke="var(--band)" stroke-width="1.6"/></svg>
        </div>
        <div class="contact-line">www.goldenhourstudio.net.au
          <svg viewBox="0 0 24 24" aria-hidden="true"><circle cx="12" cy="12" r="9"/><path d="M3 12h18M12 3c3 3 3 15 0 18M12 3c-3 3-3 15 0 18" fill="none" stroke="var(--band)" stroke-width="1.4"/></svg>
        </div>
        <div class="contact-line social"><span class="social-dot"></span>goldenhourbridals</div>
      </div>
    </div>
  </div>
</body>
</html>
```